依頼詳細
本チラシの利用シーンは、各大学の就職課・キャリアセンターへ配布したり、掲示板等に掲載してもらう予定です。
先生方へお渡しして、ゼミや研究室の学生に配布してもらったり、企業説明会で学生に直接配布する事も想定されます。弊社のホームページにも掲載の予定です。
数あるインターンシップ講座の中から、下記イメージやキーワードを目にしたときに興味を引いてもらえるようなデザインを希望します。
チラシの構成(配置)イメージを添付いたしますので、参考にしてください。
また、デザインの際にはこちらで選びました2種類の写真(別途添付)を使用してください。大きさや配置などはお任せいたします。(写真はデザイン確定後購入予定の為、ダミーです。)

<希望イメージ、キーワード>
・ IT系の会社で、『システム開発のインターンシップ』という事がひと目でわかる。
・ すっきり見やすく(絵やデザインがごちゃごちゃしていない)、さわやかなデザイン。
・ 学生目線で、親近感がわくデザインを希望します。
記載項目
下記内容は必ず記載してください。
<インターンシップ概要>
○実施期間 7月 27日(金) 8月3日(金)・10日(金) 9月7日(金)・14日(金)
※上記日程の内、いづれか1日
○募集締切 実施日の1週間前までに書類必着
○実施内容 アプリ開発で使用される人気のプログラミング言語 ”JavaScript” を使用して、全国の多くの地方自治体で利用している「文書管理システム」の開発疑似体験をしていただきます。
IT業界を知ることから、オリジナルのプログラムを通じてSEに必要とされるスキル・考え方を体感いただける内容をご用意しています。
※JavaScript言語はさほど難しいものではありませんのでプログラム経験のない方でもご参加いただけます。
○応募対象 大学院、大学、専門学校、高専に在学中のソフトウェア開発に興味がある学生
(学部、学科問わず)
○応募方法 メールにて以下の内容を記載の上、総務部)インターンシップ担当 saiyo@ktv-ltd.example.jp
宛までお送り下さい。
・名前・住所・生年月日・連絡先(携帯番号・メールアドレス)・学校名(学部学科学年)・志望理由
サイズ
A4
ページ数
片面
希望イメージ
シンプル 複雑
単色 カラフル
暗い 明るい
日常 高級
遊び心 厳粛
未来的 伝統的
女性的 男性的
希望する色
青系、水色系
納品ファイル
• イラストレーター形式 (.ai)
補足説明
※記載項目の続き

○個人情報の取り扱い ご提出いただいた個人情報はインターンシップの選考および応募者へのご連絡以外
の目的では使用いたしません。全ての個人情報は一定の保存期間経過後、弊社が責任をもって廃棄いたします。
○ ロゴマーク
○ キャッチフレーズ  誰でも作れる!業務アプリケーション開発 インターンシップ生募集!

<会社情報>
株式会社ケイ・ティ・ブイ
〒190-0047 東京都立川市栄町4-2-9 桐原栄町ビル3階
問合せ先TEL. 042-561-7304

<QRコード> (会社HPトップ画面に誘導)

※期間、締切は大きく目立つように入れて下さい。
※実施期間は修正可能なようにしてください。

今回採用させていただいたご提案は、掲示された際に目を引くという事と、男女問わず親近感が沸くイラストデザインだった事がポイントです。

この度は、多数のご応募誠にありがとうございました。
どのご提案もこちらの要望や依頼事項を汲み取って頂き、洗練されたデザインばかりでした。
はじめてのコンペで不慣れな点もあったかと思いますが、たくさんのご提案を拝見する事ができて大変感激しています。

```html
<!DOCTYPE html>
<html lang="ja">
<head>
<meta charset="utf-8">
<title>インターンシップ生募集</title>
<link href="https://fonts.googleapis.com/css2?family=Noto+Sans+JP:wght@400;500;700;900&display=swap" rel="stylesheet">
<style>
:root{
  --blue:#1f6fb8;
  --blue-dark:#174f86;
  --sky:#bfe0f4;
  --red:#a31d1d;
  --red-dark:#7c1414;
  --ink:#2a2a2a;
  --grey:#ececec;
  --white:#ffffff;
}
*{margin:0;padding:0;box-sizing:border-box}
html,body{width:849px;height:1200px;overflow:hidden;background:var(--white)}
body{font-family:"Noto Sans JP",sans-serif;color:var(--ink)}
.flyer{position:relative;width:849px;height:1200px;overflow:hidden}
.producer{position:absolute;top:0;left:0;width:100%;height:38px;display:flex;align-items:center;justify-content:center;gap:10px;font-size:13px;color:#555}
.producer .brand{font-weight:900;font-size:20px;color:var(--blue-dark);letter-spacing:1px}
.photo-team{position:absolute;top:38px;left:0;width:100%;height:262px;background:linear-gradient(120deg,#d8e6ef 0%,#9fbcd3 35%,#5d84a8 60%,#c9d9e5 100%)}
.photo-notebook{position:absolute;top:300px;left:0;width:100%;height:265px;background:linear-gradient(160deg,#e9eef1 0%,#c7d8e4 45%,#8fb2cc 100%)}
.title-band{position:absolute;top:232px;left:0;width:100%;height:58px;background:rgba(31,111,184,.55);display:flex;align-items:center;justify-content:center}
.title-band h2{color:var(--white);font-size:34px;font-weight:700;letter-spacing:2px}
.bubble{position:absolute;background:rgba(255,255,255,.9);color:var(--blue-dark);font-weight:700;font-size:14px;line-height:1.4;text-align:center;display:flex;align-items:center;justify-content:center;border-radius:50%;border:2px solid var(--sky)}
.bubble.welcome{top:48px;left:520px;width:210px;height:78px}
.bubble.project{top:112px;left:28px;width:170px;height:78px}
.bubble.field{top:318px;left:380px;width:230px;height:80px}
.recruit-band{position:absolute;top:565px;left:0;width:100%;height:98px;background:linear-gradient(180deg,var(--red) 0%,var(--red-dark) 100%);display:flex;align-items:center;justify-content:center}
.recruit-band h1{color:var(--white);font-size:62px;font-weight:900;letter-spacing:4px}
.overview{position:absolute;top:700px;left:40px;width:460px;font-size:14.5px;line-height:1.85}
.overview p{text-indent:1em;margin-bottom:6px}
.schedule{position:absolute;top:688px;left:528px;width:292px;height:262px;border:2px solid var(--red)}
.schedule-head{background:var(--red);color:var(--white);display:flex;align-items:center;gap:8px;padding:6px 10px}
.schedule-head strong{font-size:18px}
.schedule-head span{font-size:10px}
.date{display:flex;align-items:baseline;padding:4px 18px;font-weight:700;color:var(--ink)}
.date .month{font-size:30px;width:52px}
.date .day{font-size:40px;font-weight:900}
.date .dow{font-size:16px;margin-left:4px;margin-right:10px}
.date .sep{font-size:24px;margin-right:8px}
.apply{position:absolute;top:966px;left:0;width:100%;height:196px;background:var(--grey)}
.apply-title{position:absolute;top:58px;left:30px;color:var(--red);font-size:24px;font-weight:900}
.apply-body{position:absolute;top:16px;left:170px;width:410px;font-size:12.5px;line-height:1.7}
.apply-mail{display:flex;align-items:center;gap:8px;color:var(--red);font-weight:700;font-size:16px;margin-bottom:4px}
.deadline{position:absolute;top:16px;left:600px;width:220px;color:var(--red);font-weight:700;font-size:12px}
.target{position:absolute;top:42px;left:600px;width:220px;height:130px;background:var(--white);border:1px solid #ccc;padding:8px 10px;font-size:11.5px;line-height:1.6}
.target strong{color:var(--red)}
.footer{position:absolute;top:1162px;left:0;width:100%;height:38px;border-top:3px solid var(--red);display:flex;align-items:center;justify-content:center;gap:18px;font-size:12.5px}
.footer .company{font-weight:700;font-size:14px}
</style>
</head>
<body>
<div class="flyer">
  <header class="producer">
    <span>Produced by</span>
    <span class="brand">KTV</span>
    <span>Knowledge Technology Vision</span>
  </header>

  <div class="photo-team" role="img" aria-label="ノートPCを囲んで開発について話す若手社員と学生の写真"></div>
  <div class="photo-notebook" role="img" aria-label="INTERNSHIPと書かれたノートとペン、PCの置かれた机の写真"></div>

  <div class="bubble welcome">ITに興味がある方・エンジニアを<br>目指している方歓迎!</div>
  <div class="bubble project">実務に即した<br>開発プロジェクト体験!</div>
  <div class="title-band"><h2>業務アプリケーション開発体験</h2></div>
  <div class="bubble field">システム開発の現場が分かる<br>先輩社員の話が聞ける!</div>

  <section class="recruit-band"><h1>インターンシップ生募集</h1></section>

  <section class="overview">
    <p>アプリ開発で使用される人気のプログラミング言語"JavaScript"を使用して、全国の多くの地方自治体で利用している「文書管理システム」の開発疑似体験をしていただきます。</p>
    <p>IT業界を知ることから、オリジナルのプログラムを通じてSEに必要とされるスキル・考え方を体感いただける内容をご用意しています。</p>
    <p>※JavaScript言語はさほど難しいものではありませんのでプログラム経験のない方でもご参加いただけます。</p>
  </section>

  <section class="schedule">
    <div class="schedule-head"><strong>実施期間</strong><span>※下記日程の内いずれか1日</span></div>
    <div class="date"><span class="month">7/</span><span class="day">27</span><span class="dow">Fri.</span></div>
    <div class="date"><span class="month">8/</span><span class="day">3</span><span class="dow">Fri.</span><span class="sep">,</span><span class="day">10</span><span class="dow">Fri.</span></div>
    <div class="date"><span class="month">9/</span><span class="day">7</span><span class="dow">Fri.</span><span class="sep">,</span><span class="day">14</span><span class="dow">Fri.</span></div>
  </section>

  <section class="apply">
    <h3 class="apply-title">応募方法</h3>
    <div class="apply-body">
      <div class="apply-mail">
        <svg width="22" height="16" viewBox="0 0 22 16"><rect x="1" y="1" width="20" height="14" fill="none" stroke="#a31d1d" stroke-width="2"/><path d="M1 1 L11 9 L21 1" fill="none" stroke="#a31d1d" stroke-width="2"/></svg>
        saiyo@ktv-ltd.example.jp <small style="font-size:11px;color:var(--ink);font-weight:400">(総務部インターンシップ担当)</small>
      </div>
      <p>メールにて以下の内容を記載の上お送り下さい。</p>
      <p>名前/住所/生年月日/連絡先(携帯番号・メールアドレス)<br>学校名(学部学科学年)/志望理由</p>
      <p style="font-size:10.5px;margin-top:6px">ご提出いただいた個人情報はインターンシップの選考および応募者へのご連絡以外の目的では使用いたしません。</p>
    </div>
    <div class="deadline">※実施日の1週間前までに書類必着</div>
    <div class="target"><strong>応募対象</strong><br>大学院、大学、専門学校、高専に在学中のソフトウェア開発に興味がある学生<br>(学部、学科問わず)</div>
  </section>

  <footer class="footer">
    <span class="company">株式会社ケイ・ティ・ブイ</span>
    <span>TEL:042-561-7304</span>
    <span>〒190-0047 東京都立川市栄町4-2-9 桐原栄町ビル3階</span>
  </footer>
</div>
</body>
</html>
```